Powerpoint template for basic scientists studying immunology

We are an QFB-funded consortium of basic science researchers at academic centers in Boston, Philadelphia and Oxford, UK. We study why the immune system fails to get rid of Hepatitis C virus, and whether new antiviral treatments that reduce viral load improve immune function. We are looking for a powerpoint template that we can use as a "brand" for our research consortium. It would feature a logo (file attached) and should represent the fonts/colors contained in the logo. We we would present at meetings and to program officers at the QFB, but, if we ever get around to it, would also be on a website.

The scientific description is as follows:
Hepatitis C virus (HCV) infects 185 million persons worldwide, is the leading indication for liver transplantation and, in the US, has a higher mortaliy rate than HIV. The annual healthcare costs associated with HCV exceed $9 billion, a number expected to increase as the epidemic matures and end stage liver disease peaks over the next decade. By virtue of its remarkable predilection for persistence, HCV is a model chronic viral infection. Mounting evidence supports the idea that HCV, while inducing type I IFN expression, maintains chronicity by virtue of global suppression of host innate and adaptive immunity. The mainstay of treatment for the last two decades, IFN-α-based regimens are ineffective in many patient subgroups and have significant side effects. The recent development of highly effective direct acting antivirals (DAA) against HCV promises to alter the landscape of this devastating infection by offering curative therapy without IFN. However, it remains essential that we understand what type of immunity remains following pharmacological eradication of the virus because: a) many HCV infected subjects remain at risk for re-infection; and b) DAAs are only partially effective in some patient subgroups, particularly those with past treatment with IFN. The imminent availability of IFN-free treatment for HCV offers an unprecedented opportunity to understand broad questions about alterations in immunity in humans with cure of chronic infections. Until now, mechanistic dissection of human immune responses has been challenging due to limited ability to directly perturb the system. The organizing principle of this U19 Program therefore, is to capitalize on the unique opportunity to, for the first time, cure chronic viral infection in humans without immune modulation and interrogate the immunological changes that ensue. Thus, we have formulated the following central hypothesis for this Program: DAA-mediated cure of chronic HCV infection will lead to partial "resetting" of some immune abnormalities, but specific immunological defects will persist in some subjects that prevent development of optimal immunity to HCV. We will test this hypothesis through a set of integrated Projects and Cores.

Target Market(s)

scientists.

Industry/Entity Type

Biotechnology

Font styles to use
Sans Serif

Requirements
Must have
• Very clean, very simple. Mostly whitespace for puting graphs and data on. Colors, fonts should match the logo. Please see ppt example.
Should not have
• too much of the ppt covered with the logo.

```html
<!DOCTYPE html>
<html lang="en">
<head>
<meta charset="utf-8">
<title>ORV TIDE Consortium – Slide Template</title>
<link href="https://fonts.googleapis.com/css2?family=Roboto+Condensed:wght@400;700&family=Roboto:wght@400;500&display=swap" rel="stylesheet">
<style>
:root{
  --blue:#1b95d3;
  --blue-dark:#0f6fb8;
  --royal:#1f68c4;
  --green:#5fb31f;
  --green-dark:#3f8f12;
  --ink:#222;
  --grey:#8a8a8a;
  --grey-dark:#555;
  --slate:#4a5166;
  --teal-grey:#8fa3a6;
  --footer:#5e5e5e;
  --row-a:#e3e3e3;
  --row-b:#bfe3f2;
  --box:#e6f4fb;
  --page:#000;
}
*{box-sizing:border-box;margin:0;padding:0}
html,body{width:1200px;height:1200px;overflow:hidden;background:var(--page)}
body{position:relative;font-family:"Roboto",Arial,sans-serif;color:var(--grey)}
.slide{position:absolute;width:381px;height:285px;background:#fff;overflow:hidden}
.c1{left:11px}.c2{left:400px}.c3{left:789px}
.r1{top:9px}.r2{top:303px}.r3{top:597px}.r4{top:889px}
.header{position:absolute;left:0;top:0;width:100%;height:30px;background:var(--blue);display:flex;align-items:center;justify-content:space-between;padding:0 8px}
.header h1{font-family:"Roboto Condensed",Arial,sans-serif;font-weight:700;font-size:15px;color:#fff;letter-spacing:.1px}
.brand{display:flex;align-items:center;gap:4px;font-family:"Roboto",Arial,sans-serif;font-weight:400;color:#fff;font-size:11px;letter-spacing:.3px;white-space:nowrap}
.brand .dot{width:13px;height:13px;border-radius:50%;background:#fff}
.brand.large{font-size:20px;gap:7px}
.brand.large .dot{width:24px;height:24px}
.brand.colour{color:var(--blue)}
.brand.colour .dot{background:var(--green)}
.footer{position:absolute;left:0;bottom:0;width:100%;height:15px;background:var(--footer);color:#fff;font-size:6px;display:flex;align-items:center;justify-content:space-between;padding:0 4px}
.band{position:absolute;left:0;top:0;width:100%;height:166px;background:var(--blue)}
.small{font-size:6px;line-height:11px;color:var(--grey)}
.sub-title{font-family:"Roboto Condensed",Arial,sans-serif;color:var(--blue);font-size:12px;font-weight:400}
.bullet{display:inline-block;width:9px;height:9px;border-radius:50%;background:var(--green);border:2px solid var(--blue);vertical-align:-1px;margin-right:5px}
.item{position:absolute;left:14px}
.item .small{padding-left:23px}
.abs{position:absolute}
.ring-head{font-family:"Roboto Condensed",Arial,sans-serif;font-size:7.5px;color:var(--grey-dark)}
.ring-text{font-size:5.3px;line-height:8.5px;color:var(--grey)}
.tbl{position:absolute;left:32px;top:100px;width:321px;border-collapse:separate;border-spacing:0 3px;font-size:6px}
.tbl th{background:var(--blue-dark);color:#fff;font-family:"Roboto Condensed",Arial,sans-serif;font-size:8px;font-weight:700;text-align:left;padding:5px 6px}
.tbl td{padding:5px 8px;color:var(--ink)}
.tbl tr.a td{background:var(--row-a)}
.tbl tr.b td{background:var(--row-b)}
.ph{position:absolute;background:var(--box)}
.col-text{position:absolute;font-size:6.4px;line-height:11.4px;color:var(--grey-dark)}
.col-text p{margin-bottom:9px}
.thanks{background:var(--blue)}
.contact{position:absolute;left:203px;top:93px;width:178px;height:116px;background:#fff;padding:12px 16px;font-size:9px;color:var(--ink);line-height:12px}
.contact ul{list-style:none;margin-top:16px}
.contact li{display:flex;align-items:center;gap:6px;line-height:12px}
.contact svg{width:8px;height:8px}
</style>
</head>
<body>

<!-- Row 1 -->
<section class="slide c1 r1">
  <div class="band"></div>
  <h2 class="abs" style="left:18px;top:186px;font-family:'Roboto Condensed',Arial,sans-serif;font-weight:400;font-size:20px;color:var(--blue)">Project Title Here</h2>
  <p class="abs small" style="left:18px;top:214px;width:135px">Subtext here Subtext here Subtext here Subtext here Subtext here Subtext here Subtext here</p>
  <div class="abs brand large colour" style="left:266px;top:224px">ORV TIDE</div>
  <div class="footer"><span>Copyright text here</span><span>Page : 01</span></div>
</section>

<section class="slide c2 r1">
  <header class="header"><h1>PROJECT TITLE HERE</h1><div class="brand"><span class="dot"></span>ORV TIDE</div></header>
  <div class="item" style="top:54px"><h3 class="sub-title"><span class="bullet"></span>Subtext title here</h3><p class="small">Subtext here Subtext here Subtext here Subtext here Subtext here Subtext here Subtext here Subtext here<br>Subtext here Subtext here Subtext here Subtext here Subtext here Subtext here</p></div>
  <div class="item" style="top:102px"><h3 class="sub-title"><span class="bullet"></span>Subtext title here</h3><p class="small">Subtext here Subtext here Subtext here Subtext here Subtext here Subtext here Subtext here Subtext here<br>Subtext here Subtext here Subtext here Subtext here Subtext here Subtext here</p></div>
  <div class="item" style="top:150px"><h3 class="sub-title"><span class="bullet"></span>Subtext title here</h3><p class="small">Subtext here Subtext here Subtext here Subtext here Subtext here Subtext here Subtext here Subtext here<br>Subtext here Subtext here Subtext here Subtext here Subtext here Subtext here</p></div>
  <div class="item" style="top:203px"><h3 class="sub-title"><span class="bullet"></span>Subtext title here</h3><p class="small">Subtext here Subtext here Subtext here Subtext here Subtext here Subtext here Subtext here Subtext here<br>Subtext here Subtext here Subtext here Subtext here Subtext here Subtext here</p></div>
  <div class="footer"><span>Copyright text here</span><span>Page : 01</span></div>
</section>

<section class="slide c3 r1">
  <div class="band"></div>
  <h2 class="abs" style="left:220px;top:68px;font-family:'Roboto Condensed',Arial,sans-serif;font-weight:400;font-size:20px;color:#fff">Project Title Here</h2>
  <p class="abs small" style="left:220px;top:96px;width:135px;color:#fff">Subtext here Subtext here Subtext here Subtext here Subtext here Subtext here Subtext here</p>
  <div class="abs brand large colour" style="left:139px;top:228px">ORV TIDE</div>
  <div class="footer"><span>Copyright text here</span><span>Page : 01</span></div>
</section>

<!-- Row 2 -->
<section class="slide c1 r2">
  <header class="header"><h1>PROJECT TITLE HERE</h1><div class="brand"><span class="dot"></span>ORV TIDE</div></header>
  <h3 class="abs sub-title" style="left:24px;top:52px">Subtitle Here</h3>
  <p class="abs small" style="left:24px;top:70px;width:320px">Lorem ipsum dolor sit Lorem ipsum dolor sit Lorem ipsum dolor sit Lorem ipsum dolor sit Lorem ipsum dolor sit Lorem ipsum dolor sit Lorem ipsum dolor sit Lorem ipsum dolor sit</p>
  <svg class="abs" style="left:25px;top:104px" width="336" height="46" viewBox="0 0 336 46">
    <g stroke="#fff" stroke-width="1.5" fill="none">
      <polygon points="0,0 68,0 78,23 68,46 0,46" fill="var(--blue)" stroke="none"/>
      <polygon points="68,0 136,0 146,23 136,46 68,46 78,23" fill="var(--green)"/>
      <polygon points="136,0 200,0 210,23 200,46 136,46 146,23" fill="var(--royal)"/>
      <polygon points="200,0 264,0 274,23 264,46 200,46 210,23" fill="#000"/>
      <polygon points="264,0 326,0 336,23 326,46 264,46 274,23" fill="#666"/>
      <g stroke-width="1.2">
        <circle cx="37" cy="20" r="7"/><path d="M34 28h6M35 31h4"/>
        <circle cx="107" cy="20" r="7"/><path d="M104 28h6M105 31h4"/>
        <circle cx="174" cy="20" r="7"/><path d="M171 28h6M172 31h4"/>
        <circle cx="241" cy="20" r="7"/><path d="M238 28h6M239 31h4"/>
        <circle cx="303" cy="20" r="7"/><path d="M300 28h6M301 31h4"/>
      </g>
    </g>
  </svg>
  <p class="abs small" style="left:32px;top:160px;width:60px;font-size:5.5px;line-height:7.8px">Lorem ipsum dolor sit Lorem ipsum dolor sit Lorem ipsum dolor sit Lorem ipsum dolor sit Lorem ipsum dolor sit Lorem ipsum dolor sit Lorem ipsum dolor sit Lorem ipsum dolor sit</p>
  <p class="abs small" style="left:99px;top:160px;width:60px;font-size:5.5px;line-height:7.8px">Lorem ipsum dolor sit Lorem ipsum dolor sit Lorem ipsum dolor sit Lorem ipsum dolor sit Lorem ipsum dolor sit Lorem ipsum dolor sit Lorem ipsum dolor sit Lorem ipsum dolor sit</p>
  <p class="abs small" style="left:163px;top:160px;width:60px;font-size:5.5px;line-height:7.8px">Lorem ipsum dolor sit Lorem ipsum dolor sit Lorem ipsum dolor sit Lorem ipsum dolor sit Lorem ipsum dolor sit Lorem ipsum dolor sit Lorem ipsum dolor sit Lorem ipsum dolor sit</p>
  <p class="abs small" style="left:227px;top:160px;width:60px;font-size:5.5px;line-height:7.8px">Lorem ipsum dolor sit Lorem ipsum dolor sit Lorem ipsum dolor sit Lorem ipsum dolor sit Lorem ipsum dolor sit Lorem ipsum dolor sit Lorem ipsum dolor sit Lorem ipsum dolor sit</p>
  <p class="abs small" style="left:293px;top:160px;width:60px;font-size:5.5px;line-height:7.8px">Lorem ipsum dolor sit Lorem ipsum dolor sit Lorem ipsum dolor sit Lorem ipsum dolor sit Lorem ipsum dolor sit Lorem ipsum dolor sit Lorem ipsum dolor sit Lorem ipsum dolor sit</p>
  <div class="footer"><span>Copyright text here</span><span>Page : 01</span></div>
</section>

<section class="slide c2 r2">
  <header class="header"><h1>PROJECT TITLE HERE</h1><div class="brand"><span class="dot"></span>ORV TIDE</div></header>
  <svg class="abs" style="left:0;top:0" width="381" height="285" viewBox="0 0 381 285">
    <g fill="none" stroke-width="9" transform="translate(198 142)">
      <circle r="80" stroke="var(--green-dark)" stroke-dasharray="50 452.7" transform="rotate(-84)"/>
      <circle r="80" stroke="var(--green-dark)" stroke-dasharray="50 452.7" transform="rotate(-39)"/>
      <circle r="80" stroke="var(--teal-grey)" stroke-dasharray="50 452.7" transform="rotate(6)"/>
      <circle r="80" stroke="#444" stroke-dasharray="50 452.7" transform="rotate(51)"/>
      <circle r="80" stroke="var(--slate)" stroke-dasharray="50 452.7" transform="rotate(96)"/>
      <circle r="80" stroke="#555" stroke-dasharray="50 452.7" transform="rotate(141)"/>
      <circle r="80" stroke="var(--blue)" stroke-dasharray="50 452.7" transform="rotate(186)"/>
      <circle r="80" stroke="var(--blue)" stroke-dasharray="50 452.7" transform="rotate(231)"/>
    </g>
    <g fill="none" stroke="var(--blue)" stroke-width=".8">
      <path d="M70 63H110l24 24"/>
      <path d="M316 54H274l-18 22"/>
      <path d="M70 146H112"/>
      <path d="M318 130H284"/>
      <path d="M70 220H114l22-22"/>
      <path d="M318 214H274l-18-20"/>
    </g>
  </svg>
  <div class="abs brand colour" style="left:170px;top:134px;font-size:10px"><span class="dot" style="width:9px;height:9px"></span>ORV TIDE</div>
  <div class="abs" style="left:23px;top:56px;width:82px"><h4 class="ring-head">Heading Here</h4><p class="ring-text">Subtext here Subtext here Sub-text here Subtext here Subtext here Subtext here</p></div>
  <div class="abs" style="left:282px;top:47px;width:82px;text-align:right"><h4 class="ring-head">Heading Here</h4><p class="ring-text">Subtext here Subtext here Sub-text here Subtext here Subtext here Subtext here</p></div>
  <div class="abs" style="left:23px;top:139px;width:82px"><h4 class="ring-head">Heading Here</h4><p class="ring-text">Subtext here Subtext here Sub-text here Subtext here Subtext here Subtext here</p></div>
  <div class="abs" style="left:282px;top:123px;width:82px;text-align:right"><h4 class="ring-head">Heading Here</h4><p class="ring-text">Subtext here Subtext here Sub-text here Subtext here Subtext here Subtext here</p></div>
  <div class="abs" style="left:23px;top:213px;width:66px"><h4 class="ring-head">Heading Here</h4><p class="ring-text">Subtext here Subtext here Sub-text here Subtext here Subtext here Subtext here</p></div>
  <div class="abs" style="left:282px;top:207px;width:82px;text-align:right"><h4 class="ring-head">Heading Here</h4><p class="ring-text">Subtext here Subtext here Sub-text here Subtext here Subtext here Subtext here</p></div>
  <div class="footer"><span>Copyright text here</span><span>Page : 01</span></div>
</section>

<section class="slide c3 r2">
  <header class="header"><h1>PROJECT TITLE HERE</h1><div class="brand"><span class="dot"></span>ORV TIDE</div></header>
  <h3 class="abs" style="left:28px;top:53px;font-size:7.3px;font-weight:500;color:var(--royal)">Lorem ipsum dolor sit Lorem ipsum dolor sit&nbsp; Lorem ipsum dolor sit</h3>
  <p class="abs small" style="left:28px;top:67px;width:330px;font-size:5.6px;line-height:9.5px">Lorem ipsum dolor sit Lorem ipsum dolor sit Lorem ipsum dolor sit Lorem ipsum dolor sit Lorem ipsum dolor sit Lorem ipsum dolor sit Lorem ipsum dolor sit Lorem ipsum dolor sit Lorem ipsum dolor sit Lorem ipsum dolor sit Lorem ipsum dolor sit Lorem ipsum dolor sit Lorem ipsum dolor sit Lorem ipsum dolor sit</p>
  <div class="abs small" style="left:28px;top:106px;font-size:5.6px;line-height:18px">Lorem ipsum dolor sit<br>Lorem ipsum dolor sit<br>Lorem ipsum dolor sit<br>Lorem ipsum dolor sit<br>Lorem ipsum dolor sit<br>Lorem ipsum dolor sit<br><span style="display:block;margin-top:24px">Lorem ipsum dolor sit</span></div>
  <svg class="abs" style="left:86px;top:120px" width="290" height="130" viewBox="0 0 290 130">
    <rect x="0" y="76" width="15" height="44" fill="var(--green-dark)"/>
    <rect x="23" y="46" width="20" height="74" fill="#555"/>
    <rect x="48" y="61" width="19" height="59" fill="var(--blue)"/>
    <rect x="72" y="86" width="19" height="34" fill="var(--royal)"/>
    <rect x="96" y="110" width="21" height="10" fill="var(--green-dark)"/>
    <rect x="121" y="116" width="23" height="4" fill="#777"/>
    <rect x="149" y="4" width="19" height="116" fill="var(--blue)"/>
    <rect x="174" y="110" width="21" height="10" fill="var(--green-dark)"/>
    <rect x="200" y="115" width="20" height="5" fill="#999"/>
    <rect x="224" y="116" width="23" height="4" fill="#888"/>
  </svg>
  <div class="footer"><span>Copyright text here</span><span>Page : 01</span></div>
</section>

<!-- Row 3 -->
<section class="slide c1 r3">
  <header class="header"><h1>PROJECT TITLE HERE</h1><div class="brand"><span class="dot"></span>ORV TIDE</div></header>
  <h3 class="abs sub-title" style="left:8px;top:50px;font-weight:700;font-size:10px"><span class="bullet"></span>Table Head Here</h3>
  <p class="abs small" style="left:32px;top:64px;width:330px;font-size:5.6px;line-height:8.2px">Lorem ipsum dolor sit Lorem ipsum dolor sit Lorem ipsum dolor sit Lorem ipsum dolor sit Lorem ipsum dolor sit Lorem ipsum dolor sit Lorem ipsum dolor sit Lorem ipsum dolor sit Lorem ipsum dolor sit Lorem ipsum dolor sit Lorem ipsum dolor sit Lorem ipsum dolor sit Lorem ipsum dolor sit Lorem ipsum dolor sit</p>
  <table class="tbl">
    <thead><tr><th>TABLE HEAD HERE</th><th>TABLE HEAD HERE</th><th style="text-align:right">TABLE HEAD HERE</th></tr></thead>
    <tbody>
      <tr class="a"><td>Subtext here Subtext here</td><td>Subtext here Subtext here</td><td style="text-align:right">Subtext here Subtext here</td></tr>
      <tr class="b"><td>Subtext here Subtext here</td><td>Subtext here Subtext here</td><td style="text-align:right">Subtext here Subtext here</td></tr>
      <tr class="a"><td>Subtext here Subtext here</td><td>Subtext here Subtext here</td><td style="text-align:right">Subtext here Subtext here</td></tr>
      <tr class="b"><td>Subtext here Subtext here</td><td>Subtext here Subtext here</td><td style="text-align:right">Subtext here Subtext here</td></tr>
      <tr class="a"><td>Subtext here Subtext here</td><td>Subtext here Subtext here</td><td style="text-align:right">Subtext here Subtext here</td></tr>
      <tr class="b"><td>Subtext here Subtext here</td><td>Subtext here Subtext here</td><td style="text-align:right">Subtext here Subtext here</td></tr>
    </tbody>
  </table>
  <div class="footer"><span>Copyright text here</span><span>Page : 01</span></div>
</section>

<section class="slide c2 r3">
  <header class="header"><h1>PROJECT TITLE HERE</h1><div class="brand"><span class="dot"></span>ORV TIDE</div></header>
  <h3 class="abs sub-title" style="left:8px;top:50px;font-weight:700;font-size:10.5px"><span class="bullet"></span>Subtext title here</h3>
  <div class="col-text" style="left:27px;top:64px;width:150px">
    <p>Subtext here Subtext here Subtext here Subtext here Subtext here Subtext here Subtext here Subtext here<br>Subtext here Subtext here Subtext here Subtext here</p>
    <p>Subtext here Subtext here Subtext here Subtext here Subtext here Subtext here Subtext here Subtext here<br>Subtext here Subtext here Subtext here Subtext here</p>
    <p>Subtext here Subtext here Subtext here Subtext here Subtext here Subtext here Subtext here Subtext here<br>Subtext here Subtext here Subtext here Subtext here</p>
  </div>
  <div class="ph" style="left:200px;top:56px;width:165px;height:91px"></div>
  <div class="ph" style="left:200px;top:154px;width:165px;height:91px"></div>
  <div class="footer"><span>Copyright text here</span><span>Page : 01</span></div>
</section>

<section class="slide c3 r3 thanks">
  <div class="abs brand large" style="left:40px;top:165px">ORV TIDE</div>
  <h2 class="abs" style="left:203px;top:74px;font-family:'Roboto Condensed',Arial,sans-serif;font-weight:400;font-size:12px;color:#fff;white-space:nowrap">THANKS FOR YOUR VALUABL TIME</h2>
  <div class="contact">
    <p>Lorem ipsum dolor sit amet,<br>consectetur adipiscing elit.<br>Donec accumsan.</p>
    <ul>
      <li><svg viewBox="0 0 10 10"><path d="M2 1l2 2-1 1.5c.8 1.6 1.9 2.7 3.5 3.5L8 6l2 2-1.5 2C4.5 9.5.5 5.5 0 1.5z" fill="var(--ink)"/></svg>: 555 0192 3864</li>
      <li><svg viewBox="0 0 10 10"><rect x="0" y="2" width="10" height="7" fill="var(--ink)"/><path d="M0 2l5 4 5-4" stroke="#fff" fill="none"/></svg>: abcde@postline.net</li>
      <li><svg viewBox="0 0 10 10"><path d="M10 0L0 4l4 2 2 4z" fill="var(--ink)"/></svg>: abcdepostline.net</li>
    </ul>
  </div>
</section>

<!-- Row 4 -->
<section class="slide c1 r4">
  <header class="header"><h1>PROJECT TITLE HERE</h1><div class="brand"><span class="dot"></span>ORV TIDE</div></header>
  <h3 class="abs sub-title" style="left:8px;top:50px;font-weight:700;font-size:10.5px"><span class="bullet"></span>Subtext title here</h3>
  <div class="col-text" style="left:27px;top:64px;width:150px">
    <p>Subtext here Subtext here Subtext here Subtext here Subtext here Subtext here Subtext here Subtext here<br>Subtext here Subtext here Subtext here Subtext here</p>
    <p>Subtext here Subtext here Subtext here Subtext here Subtext here Subtext here Subtext here Subtext here<br>Subtext here Subtext here Subtext here Subtext here</p>
    <p>Subtext here Subtext here Subtext here Subtext here Subtext here Subtext here Subtext here Subtext here<br>Subtext here Subtext here Subtext here Subtext here</p>
  </div>
  <h3 class="abs sub-title" style="left:199px;top:50px;font-weight:700;font-size:10.5px"><span class="bullet"></span>Subtext title here</h3>
  <div class="col-text" style="left:218px;top:64px;width:150px">
    <p>Subtext here Subtext here Subtext here Subtext here Subtext here Subtext here Subtext here Subtext here<br>Subtext here Subtext here Subtext here Subtext here</p>
    <p>Subtext here Subtext here Subtext here Subtext here Subtext here Subtext here Subtext here Subtext here<br>Subtext here Subtext here Subtext here Subtext here</p>
    <p>Subtext here Subtext here Subtext here Subtext here Subtext here Subtext here Subtext here Subtext here<br>Subtext here Subtext here Subtext here Subtext here</p>
  </div>
  <div class="footer"><span>Copyright text here</span><span>Page : 01</span></div>
</section>

<section class="slide c2 r4">
  <header class="header"><h1>PROJECT TITLE HERE</h1><div class="brand"><span class="dot"></span>ORV TIDE</div></header>
  <div class="footer"><span>Copyright text here</span><span>Page : 01</span></div>
</section>

</body>
</html>
```